WWW.VELTRONA.IT BUSINNES CARD

WE NEED A BUSINESS CARD . I HAVE A COMPANY IN ITALY NR 1 IN HAIR MEDICAL CARE AN HAIR REPLECEMENT . IN CARD I NEED WRITE WEB ADDRESS, MAIL , ADDRESS, TELEPHONE NUMBER , AND NAME
IN THE BACK SIDE I NEED MY DOCTOR LOGO .
MY WEB SITE IS WWW.VELTRONA.IT
Updates

Target Market(s)

CONSUMER B2C

Industry/Entity Type

Hair And Beauty

Contact Information for Business Card

I WANT A MEDICAL BUSINESS CARD.

Font styles to use
Other font styles liked:
• VERDANA

Colors
33a6d7
3176b5
85abd2
aedbee
eaf1f7
ffffff

Requirements
Must have
• I NEED MY LOGO AND LOGO OF DR VELTRONA

```html
<!DOCTYPE html>
<html lang="it">
<head>
<meta charset="utf-8">
<title>Veltrona – Biglietto da visita</title>
<link href="https://fonts.googleapis.com/css2?family=Noto+Sans:wght@400;700&display=swap" rel="stylesheet">
<style>
  :root{
    --blue-deep:#1f73bd;
    --blue-mid:#3176b5;
    --blue-bright:#1e8fe8;
    --blue-sky:#33a6d7;
    --blue-pale:#85abd2;
    --blue-ice:#aedbee;
    --paper:#f2f2f2;
    --white:#ffffff;
    --ink:#5a5a5a;
    --ink-dark:#4a4a4a;
    --stage:#e6e7e8;
    --mascot-brown:#7a4320;
    --mascot-floor:#e9b08c;
  }
  *{box-sizing:border-box;margin:0;padding:0}
  html,body{width:1200px;height:900px;overflow:hidden}
  body{background:var(--stage);font-family:"Noto Sans",Verdana,sans-serif;position:relative}

  .card{position:absolute;left:250px;width:700px;height:400px;overflow:hidden;box-shadow:0 4px 14px rgba(0,0,0,.15)}
  .card--front{top:35px;background:var(--white)}
  .card--back{top:465px;background:var(--paper)}

  /* front */
  .front-square{position:absolute;background:var(--blue-bright)}
  .front-square--a{left:0;top:0;width:70px;height:60px;opacity:.85}
  .front-square--b{left:40px;top:50px;width:60px;height:55px;opacity:.6}
  .front-band{position:absolute;left:0;top:220px;width:430px;height:70px;background:var(--blue-bright)}
  .front-band__shade{position:absolute;left:0;top:0;width:120px;height:100%;background:var(--blue-deep)}
  .front-band__url{position:absolute;right:30px;top:50%;transform:translateY(-50%);color:var(--white);font-weight:700;font-size:30px;letter-spacing:1px}
  .brand{position:absolute;left:360px;top:110px;width:300px}
  .brand__row{display:flex;align-items:center;gap:10px}
  .brand__mark{width:26px;height:26px;background:var(--blue-sky)}
  .brand__name{font-weight:700;font-size:44px;color:var(--blue-bright);line-height:1}
  .brand__tagline{margin-top:8px;font-size:11px;letter-spacing:1.5px;color:var(--blue-mid)}

  /* back */
  .mascot{position:absolute;left:30px;top:20px;width:132px;height:350px;border-radius:60px 60px 50% 50%/40px 40px 30px 30px;background:linear-gradient(180deg,var(--mascot-brown) 0%,#9a5a30 60%,var(--mascot-floor) 100%)}
  .doctor-name{position:absolute;left:188px;top:322px;transform-origin:left top;transform:rotate(-90deg);font-weight:700;font-style:italic;font-size:22px;color:var(--blue-mid);white-space:nowrap}
  .band{position:absolute;left:222px;top:0;width:77px;height:400px;background:var(--blue-deep)}
  .band__light{position:absolute;left:0;width:100%;background:var(--blue-bright)}
  .band__light--a{top:85px;height:27px;opacity:.7}
  .band__light--b{top:112px;height:190px}
  .band__light--c{top:302px;height:27px;opacity:.7}

  .contacts{position:absolute;right:103px;top:18px;text-align:right;color:var(--ink)}
  .office{margin-bottom:14px}
  .office__city{font-weight:700;font-size:21px;color:var(--ink-dark);line-height:1.15}
  .office__line{font-size:15px;line-height:1.25}
  .office__phone{color:var(--blue-sky);font-weight:700}
  .contact-line{position:absolute;right:103px;font-weight:700;font-size:23px;color:var(--ink-dark)}
  .contact-line--mail{top:248px}
  .contact-line--web{top:323px}
  .icon{position:absolute;right:40px}
  .icon--people{top:20px}
  .icon--mail{top:250px}
  .icon--web{top:322px}
</style>
</head>
<body>

<section class="card card--front" aria-label="Fronte del biglietto">
  <div class="front-square front-square--a"></div>
  <div class="front-square front-square--b"></div>
  <div class="front-band">
    <div class="front-band__shade"></div>
    <span class="front-band__url">www.veltrona.it</span>
  </div>
  <div class="brand">
    <div class="brand__row">
      <span class="brand__mark"></span>
      <span class="brand__name">VELTRONA</span>
    </div>
    <p class="brand__tagline">CURA E REINTEGRAZIONE DEI CAPELLI</p>
  </div>
</section>

<section class="card card--back" aria-label="Retro del biglietto">
  <div class="mascot" role="img" aria-label="Illustrazione della mascotte dr. Veltrona"></div>
  <span class="doctor-name">dr. Veltrona</span>
  <div class="band">
    <div class="band__light band__light--a"></div>
    <div class="band__light band__light--b"></div>
    <div class="band__light band__light--c"></div>
  </div>

  <div class="contacts">
    <div class="office">
      <p class="office__city">Firenze</p>
      <p class="office__line">Via Lorenzetti 142/9</p>
      <p class="office__line">Telp. <span class="office__phone">055 4172968</span></p>
    </div>
    <div class="office">
      <p class="office__city">Livorno</p>
      <p class="office__line">Via dei Mulini 317</p>
      <p class="office__line">Telp. <span class="office__phone">0586 731520</span></p>
    </div>
    <div class="office">
      <p class="office__city">Verona</p>
      <p class="office__line">Via Corsini 48</p>
      <p class="office__line">Telp. <span class="office__phone">055 4172968</span></p>
    </div>
  </div>

  <p class="contact-line contact-line--mail">info@veltrona.it</p>
  <p class="contact-line contact-line--web">www.veltrona.it</p>

  <svg class="icon icon--people" width="44" height="56" viewBox="0 0 44 56" aria-hidden="true">
    <circle cx="27" cy="10" r="8" fill="var(--blue-pale)"/>
    <path d="M14 38 Q14 20 27 20 Q40 20 40 38 Z" fill="var(--blue-pale)"/>
    <circle cx="17" cy="13" r="9" fill="var(--blue-bright)"/>
    <path d="M2 42 Q2 23 17 23 Q32 23 32 42 Z" fill="var(--blue-bright)"/>
    <rect x="2" y="45" width="38" height="9" fill="var(--blue-ice)"/>
  </svg>
  <svg class="icon icon--mail" width="42" height="46" viewBox="0 0 42 46" aria-hidden="true">
    <rect x="1" y="1" width="40" height="28" fill="var(--blue-bright)"/>
    <path d="M1 1 L21 17 L41 1 M1 29 L16 14 M41 29 L26 14" fill="none" stroke="var(--white)" stroke-width="2"/>
    <rect x="1" y="33" width="40" height="11" fill="var(--blue-ice)"/>
  </svg>
  <svg class="icon icon--web" width="42" height="52" viewBox="0 0 42 52" aria-hidden="true">
    <rect x="2" y="2" width="28" height="16" rx="3" fill="var(--blue-bright)"/>
    <text x="16" y="14" font-size="8" font-weight="700" fill="var(--white)" text-anchor="middle" font-family="Noto Sans, sans-serif">WEB</text>
    <path d="M14 22 L34 38 L26 40 L30 48 L26 50 L22 42 L16 46 Z" fill="var(--blue-deep)"/>
  </svg>
</section>

</body>
</html>
```